.

Target Market(s)

Young, male, tech savvy, cryptocurrency investors

Industry/Entity Type

Information Technology

Logo Text

.

Coding

Coded - Design and coding required

Number of Pages Required

1 page

Font styles to use
Sans Serif

Colors

Designer to choose colors to be used in the design.

Requirements
Must have
• .

```html
<!DOCTYPE html>
<html lang="en">
<head>
<meta charset="utf-8">
<title>Zorvex Network</title>
<link rel="stylesheet" href="https://fonts.googleapis.com/css2?family=Poppins:wght@400;500;600;700&display=swap">
<style>
  :root {
    --bg-deep: #1d0d02;
    --bg-black: #0b0502;
    --gold: #f5b53a;
    --gold-soft: #e6a13a;
    --amber: #c9771c;
    --green: #0bb55a;
    --white: #ffffff;
    --text-light: #f3ece4;
  }
  * { box-sizing: border-box; margin: 0; padding: 0; }
  html, body {
    width: 1034px; height: 1200px; overflow: hidden;
    background: var(--bg-deep);
    font-family: "Poppins", sans-serif;
    color: var(--white);
  }
  .page { position: relative; width: 1034px; height: 1200px; }

  /* Hero */
  .hero { position: absolute; left: 0; top: 0; width: 1034px; height: 559px; overflow: hidden; }
  .hero-art {
    position: absolute; inset: 0;
    background:
      radial-gradient(ellipse 260px 260px at 516px 300px, rgba(170,120,40,.55), transparent 70%),
      radial-gradient(ellipse 180px 40px at 780px 318px, rgba(255,200,80,.45), transparent 70%),
      radial-gradient(ellipse 300px 200px at 120px 420px, rgba(140,80,20,.35), transparent 70%),
      radial-gradient(ellipse 300px 220px at 900px 120px, rgba(160,90,20,.35), transparent 70%),
      linear-gradient(180deg, #2a1505 0%, #1f0f04 60%, #2a1606 100%);
  }
  .logo { position: absolute; left: 124px; top: 48px; text-align: center; }
  .logo-name { font-size: 34px; font-weight: 500; color: var(--gold); line-height: 1; letter-spacing: -0.5px; }
  .logo-sub { font-size: 10px; font-weight: 500; letter-spacing: 6px; color: var(--white); margin-top: 4px; padding-left: 6px; }
  .menu-btn {
    position: absolute; left: 884px; top: 45px; width: 35px; height: 44px;
    border: 2px solid var(--gold); border-radius: 18px;
    display: flex; align-items: center; justify-content: center;
    background: rgba(0,0,0,.5);
  }
  .hero-content { position: absolute; left: 0; right: 0; top: 220px; text-align: center; }
  .hero-title { font-size: 43px; font-weight: 700; line-height: 42px; }
  .hero-sub { font-size: 21px; font-weight: 400; margin-top: 10px; }
  .btn {
    display: inline-flex; align-items: center; justify-content: center;
    background: var(--green); color: var(--white);
    font-family: "Poppins", sans-serif; font-weight: 600;
    border: none; border-radius: 24px;
  }
  .hero-cta { width: 190px; height: 44px; font-size: 14px; margin-top: 20px; }
  .scroll-down { position: absolute; left: 503px; top: 459px; }

  /* Timeline */
  .timeline { position: absolute; left: 0; top: 559px; width: 1034px; height: 350px; background: var(--bg-deep); }
  .milestones { position: absolute; left: 108px; top: 58px; display: flex; gap: 19px; }
  .milestone { width: 259px; text-align: center; }
  .milestone-photo { width: 259px; height: 163px; }
  .photo-coins-silver { background: radial-gradient(circle at 45% 50%, #b9b2a4, #5a5349 55%, #1c1a17); }
  .photo-coins-gold { background: radial-gradient(circle at 50% 45%, #d4a44e, #7a5520 50%, #2a1a0a); }
  .photo-crowd { background: radial-gradient(circle at 65% 10%, #fff0b8, #f0a530 35%, #a55818 70%, #5c2a10); }
  .milestone-date { font-size: 17px; font-weight: 600; color: var(--gold); margin-top: 7px; line-height: 26px; }
  .milestone-text { font-size: 11px; color: var(--text-light); margin-top: 0; line-height: 18px; }

  /* Signup */
  .signup { position: absolute; left: 0; top: 909px; width: 1034px; height: 210px; overflow: hidden; }
  .signup-art {
    position: absolute; inset: 0;
    background:
      linear-gradient(160deg, transparent 30%, rgba(230,140,40,.35) 45%, transparent 55%),
      linear-gradient(20deg, transparent 40%, rgba(230,140,40,.3) 50%, transparent 60%),
      linear-gradient(180deg, #120803 0%, #3a1c06 50%, #160a03 100%);
  }
  .signup-title { position: absolute; left: 0; right: 0; top: 24px; text-align: center; font-size: 32px; font-weight: 600; }
  .signup-form {
    position: absolute; left: 191px; top: 89px; width: 652px; height: 62px;
    border: 1px solid var(--amber); background: rgba(0,0,0,.82);
    display: flex; align-items: center; justify-content: space-between; padding: 0 9px 0 26px;
  }
  .signup-input { font-size: 11px; color: var(--white); }
  .signup-btn { width: 190px; height: 44px; font-size: 14px; }

  /* Footer */
  .footer { position: absolute; left: 0; top: 1119px; width: 1034px; height: 81px;
    background: linear-gradient(180deg, #160a03 0%, var(--bg-black) 40%);
    text-align: center; padding-top: 47px; font-size: 11px; font-weight: 600; line-height: 18px; }
</style>
</head>
<body>
<div class="page">
  <header class="hero">
    <div class="hero-art" role="img" aria-label="Golden glowing coin with circuit pattern and network lines"></div>
    <div class="logo">
      <div class="logo-name">Zorvex</div>
      <div class="logo-sub">NETWORK</div>
    </div>
    <div class="menu-btn" aria-label="Menu">
      <svg width="16" height="12" viewBox="0 0 16 12"><rect y="0" width="16" height="2" fill="#fff"/><rect y="5" width="16" height="2" fill="#fff"/><rect y="10" width="16" height="2" fill="#fff"/></svg>
    </div>
    <div class="hero-content">
      <h1 class="hero-title">The world’s most<br>advanced blockchain</h1>
      <p class="hero-sub">The widest token distribution</p>
      <button class="btn hero-cta">Get Started Today</button>
    </div>
    <svg class="scroll-down" width="28" height="28" viewBox="0 0 28 28" aria-label="Scroll down">
      <circle cx="14" cy="14" r="12" fill="none" stroke="#f5b53a" stroke-width="1.8"/>
      <path d="M9 12l5 5 5-5" fill="none" stroke="#f5b53a" stroke-width="1.8"/>
    </svg>
  </header>

  <section class="timeline">
    <div class="milestones">
      <div class="milestone">
        <div class="milestone-photo photo-coins-silver" role="img" aria-label="Silver crypto coins"></div>
        <div class="milestone-date">Sept 2017</div>
        <div class="milestone-text">Velmora Network Airdrop</div>
      </div>
      <div class="milestone">
        <div class="milestone-photo photo-coins-gold" role="img" aria-label="Gold crypto coins on circuit board"></div>
        <div class="milestone-date">Oct 2017</div>
        <div class="milestone-text">Kestrane Network Linked Address Airdrop</div>
      </div>
      <div class="milestone">
        <div class="milestone-photo photo-crowd" role="img" aria-label="Silhouettes of people celebrating at sunset"></div>
        <div class="milestone-date">Nov 2017</div>
        <div class="milestone-text">Proof-of-Individuality Human Airdrop</div>
      </div>
    </div>
  </section>

  <section class="signup">
    <div class="signup-art" role="img" aria-label="Glowing amber light streaks"></div>
    <h2 class="signup-title">Signup Now</h2>
    <div class="signup-form">
      <span class="signup-input">Enter Your E-mail Address</span>
      <button class="btn signup-btn">Subscribe Now</button>
    </div>
  </section>

  <footer class="footer">© 2017 Company Name &nbsp;|&nbsp;&nbsp; All Rights Reserved</footer>
</div>
</body>
</html>
```